Word template Letterhead for Australian Law Firm

We are a small law firm based in Manly, NSW, Australia. We have had a new logo designed for us and wish to freshen up the appearance of our letterhead. We require the letterhead to be in a word document that we can type over. This will not be a ‘printed’ letterhead because we send the majority of our correspondence via email. We would like to see a few options. We have attached our previous letterhead as well as the artwork for our new logo. We like the idea of a watermark across the bottom of the letter but the watermark must stay in place and we must be able to type over it. We are open to some colour throughout the letterhead because the majority of our correspondence is sent electronically. We also use electronic signatures. I have uploaded an example of this.The letterhead must include:-1. Our address details – including our phone number, physical address, website address etc. These details can be found on the copy of our previous letterhead;2. ABN Number;3. The words ‘Brevicor (NSW) Pty Ltd ACN 482 731 058 trading as Shipton & AssociatesLiability limited by a scheme approved under Professional Standards Legislation. The letterhead does not need to include the names and qualifications of the people working at the firm. Thank you.

Target Market(s)

Clients and other parties

Industry/Entity Type

Law Firm

Font styles to use
Other font styles liked:
• raleway, montserrat

Colors

Designer to choose colors to be used in the design.

Requirements
Must have
• Certain wording - please see project description.
• Must be a word document and must be able to type over the watermark etc.
Nice to have
• Watermark at the bottom of the letter.

```html
<!DOCTYPE html>
<html lang="en">
<head>
<meta charset="utf-8">
<title>Kervell &amp; Associates Letterhead</title>
<link rel="stylesheet" href="https://fonts.googleapis.com/css2?family=Open+Sans:wght@400;700&family=Source+Sans+3:wght@400;700&display=swap">
<style>
  :root {
    --paper: #ffffff;
    --ink: #3a3a3a;
    --ink-dark: #222222;
    --heading: #6e6e6e;
    --accent: #0e70b8;
    --brand: #5a6bb8;
    --rule: #333333;
  }
  * { box-sizing: border-box; margin: 0; padding: 0; }
  html, body { width: 980px; height: 1200px; overflow: hidden; background: var(--paper); }
  .letterhead { position: relative; width: 980px; height: 1200px; background: var(--paper); }

  .brand { position: absolute; left: 88px; top: 108px; display: flex; align-items: center; gap: 10px; }
  .brand-dot { width: 22px; height: 22px; border-radius: 50%; background: var(--brand); }
  .brand-name { font-family: "Open Sans", sans-serif; font-weight: 700; font-size: 17px; letter-spacing: 1px; color: var(--brand); }

  .letter { position: absolute; left: 87px; top: 240px; width: 807px; font-family: "Source Sans 3", sans-serif; color: var(--ink); }
  .letter-title { font-size: 22px; font-weight: 700; color: var(--heading); margin-bottom: 14px; }
  .letter-body p { font-size: 16px; line-height: 20.4px; text-align: justify; hyphens: auto; margin-bottom: 20.4px; }
  .letter-body p.continues { height: 81.6px; overflow: hidden; text-align-last: justify; margin-bottom: 0; }

  .contact { position: absolute; left: 88px; top: 1024px; width: 812px; display: flex; justify-content: space-between; font-family: "Open Sans", sans-serif; font-weight: 700; font-size: 12px; line-height: 16px; color: var(--ink-dark); }
  .contact-item { display: flex; align-items: flex-start; gap: 12px; }
  .contact-icon { width: 40px; height: 40px; border-radius: 50%; background: var(--accent); display: flex; align-items: center; justify-content: center; flex: none; margin-top: -2px; }
  .contact-item:nth-child(1) { width: 240px; }
  .contact-item:nth-child(2) { width: 240px; }

  .footer-rule { position: absolute; left: 88px; top: 1090px; width: 818px; border-top: 2px solid var(--rule); }

  .legal { position: absolute; left: 133px; top: 1110px; display: flex; align-items: center; gap: 28px; font-family: "Open Sans", sans-serif; font-size: 14px; line-height: 17px; color: var(--ink-dark); }
  .accreditation-badge { width: 70px; height: 70px; border-radius: 50%; background: #1a1a1a; border: 6px solid #d7e7f3; flex: none; }
</style>
</head>
<body>
<main class="letterhead">
  <header class="brand">
    <span class="brand-dot"></span>
    <span class="brand-name">Kervell &amp; Associates</span>
  </header>

  <article class="letter">
    <h1 class="letter-title">Lorem ipsum dolor sit amet</h1>
    <div class="letter-body">
      <p>Lorem ipsum dolor sit amet, consectetur adipiscing elit, sed do eiusmod tempor incididunt ut labore et dolore magna aliqua. Ut enim ad minim veniam, quis nostrud exercitation ullamco laboris nisi ut aliquip ex ea commodo consequat. Duis aute irure dolor in reprehenderit in voluptate velit esse cillum dolore eu fugiat nulla pariatur. Excepteur sint occaecat cupidatat non proident, sunt in culpa qui officia deserunt mollit anim id est laborum Sed ut perspiciatis unde omnis iste natus error sit voluptatem accusantium doloremque laudantium, totam rem aperiam, eaque ipsa quae ab illo inventore veritatis et quasi architecto beatae vitae dicta sunt explicabo. Nemo enim ipsam voluptatem quia voluptas sit aspernatur aut odit aut fugit, sed quia consequuntur magni dolores eos qui ratione voluptatem sequi nesciunt. Neque porro quisquam est, qui dolorem ipsum quia dolor sit amet, consectetur, adipisci velit, sed quia non numquam eius modi tempora incidunt ut labore et dolore magnam aliquam quaerat voluptatem. Ut enim ad minima veniam, quis nostrum exercitationem ullam corporis suscipit laboriosam, nisi ut aliquid ex ea commodi consequatur? Quis autem vel eum iure reprehenderit qui in ea voluptate velit esse quam nihil molestiae consequatur, vel illum qui dolorem eum fugiat quo voluptas nulla pariatur?</p>
      <p>Lorem ipsum dolor sit amet, consectetur adipiscing elit, sed do eiusmod tempor incididunt ut labore et dolore magna aliqua. Ut enim ad minim veniam, quis nostrud exercitation ullamco laboris nisi ut aliquip ex ea commodo consequat. Duis aute irure dolor in reprehenderit in voluptate velit esse cillum dolore eu fugiat nulla pariatur. Excepteur sint occaecat cupidatat non proident, sunt in culpa qui officia deserunt mollit anim id est laborum Sed ut perspiciatis unde omnis iste natus error sit voluptatem accusantium doloremque laudantium, totam rem aperiam, eaque ipsa quae ab illo inventore veritatis et quasi architecto beatae vitae dicta sunt explicabo. Nemo enim ipsam voluptatem quia voluptas sit aspernatur aut odit aut fugit, sed quia consequuntur magni dolores eos qui ratione voluptatem sequi nesciunt. Neque porro quisquam est, qui dolorem ipsum quia dolor sit amet, consectetur, adipisci velit, sed quia non numquam eius modi tempora incidunt ut labore et dolore magnam aliquam quaerat voluptatem. Ut enim ad minima veniam, quis nostrum exercitationem ullam corporis suscipit laboriosam, nisi ut aliquid ex ea commodi consequatur? Quis autem vel eum iure reprehenderit qui in ea voluptate velit esse quam nihil molestiae consequatur, vel illum qui dolorem eum fugiat quo voluptas nulla pariatur?</p>
      <p class="continues">Lorem ipsum dolor sit amet, consectetur adipiscing elit, sed do eiusmod tempor incididunt ut labore et dolore magna aliqua. Ut enim ad minim veniam, quis nostrud exercitation ullamco laboris nisi ut aliquip ex ea commodo consequat. Duis aute irure dolor in reprehenderit in voluptate velit esse cillum dolore eu fugiat nulla pariatur. Excepteur sint occaecat cupidatat non proident, sunt in culpa qui officia deserunt mollit anim id est laborum sed ut perspiciatis unde omnis iste natus error sit voluptatem.</p>
    </div>
  </article>

  <section class="contact">
    <div class="contact-item">
      <span class="contact-icon">
        <svg width="18" height="22" viewBox="0 0 18 22" aria-hidden="true"><path d="M9 1C4.6 1 1.5 4.2 1.5 8.4 1.5 13.6 9 21 9 21s7.5-7.4 7.5-12.6C16.5 4.2 13.4 1 9 1z" fill="#fff"/><circle cx="9" cy="8.4" r="2.8" fill="#0e70b8"/></svg>
      </span>
      <address style="font-style:normal">Suite 4, 22 Corella Street<br>Tarrin NSW 2099<br>ABN: 31 482 731 058</address>
    </div>
    <div class="contact-item">
      <span class="contact-icon">
        <svg width="20" height="20" viewBox="0 0 24 24" aria-hidden="true"><path d="M6.6 10.8a15.1 15.1 0 0 0 6.6 6.6l2.2-2.2a1 1 0 0 1 1-.25 11.4 11.4 0 0 0 3.6.57 1 1 0 0 1 1 1V20a1 1 0 0 1-1 1A17 17 0 0 1 3 4a1 1 0 0 1 1-1h3.5a1 1 0 0 1 1 1c0 1.25.2 2.45.57 3.57a1 1 0 0 1-.25 1z" fill="#fff"/></svg>
      </span>
      <div>TELEPHONE: (02) 9041 3318<br>FACSIMILE: (02) 9041 3319</div>
    </div>
    <div class="contact-item">
      <span class="contact-icon">
        <svg width="20" height="20" viewBox="0 0 20 20" aria-hidden="true" fill="none" stroke="#fff" stroke-width="1.4"><circle cx="10" cy="10" r="8"/><ellipse cx="10" cy="10" rx="3.5" ry="8"/><line x1="2" y1="10" x2="18" y2="10"/><line x1="3.2" y1="6" x2="16.8" y2="6"/><line x1="3.2" y1="14" x2="16.8" y2="14"/></svg>
      </span>
      <div>Email: reception@brevicor.com.au<br>www.kervellassociates.com.au</div>
    </div>
  </section>

  <hr class="footer-rule">

  <footer class="legal">
    <span class="accreditation-badge" role="img" aria-label="Accreditation badge"></span>
    <p>Brevicor (NSW) Pty Ltd ACN 482 731 058 trading as Kervell &amp; AssociatesLiability limited<br>by a scheme approved under Professional Standards Legislation</p>
  </footer>
</main>
</body>
</html>
```